Photography Company Seeks Amazing and Fun Website Design

Note: This is for design only. No coding required. We want to see your ideas for a great website! This will be a FUN design and not boring like others you may work on.

Please let your creative ideas flow. We have given you a ton of info along with videos to help you understand what we are after, however we WANT your creativity to shine through in your designs!

We are a professional company that has run hundreds of crowdsourced projects on multiple platforms. If you participate in this contest (we hope you do) you can expect great video feedback, consistent feedback, and also our guarantee that if we know your website design will not be what we are looking for we will notify you so you don’t waste your time if there is no chance of you winning.

We respect and recognize this is how you make your living and we will not play games. We look forward to an awesome contest and awesome website designs.

Design Brief:

We are looking for a stunning website design to showcase this amazing photography company. Their current site is:

http://www.kelvaprints.example/

As you can see they do amazing photography and need an amazing website to showcase their work and to attract new people into their studios.

We are looking to get a website that is clean, classy, bright, artistic, and that really helps this company stand out amongst other photography companies.

We need a homepage and an interior page mockup.

Here are some examples of other sites in their business with what we like:

http://www.tabrowenstudio.example/

Please watch video to learn what we like and don’t like:http://clipvault.example/t/QpR4sz7LmWd

http://www.holbrinkimaging.example/

Please watch video to learn what we like and don’t like: http://clipvault.example/t/Hb8ufN2kxyPa

NOTE: We do not want to copy anything outright. We want to learn, model and take their ideas and make them better. We also want to be flexible and take what we like along with your creativity to make an amazing design.

Here is what we are looking for in more specific terms:

NOTE: Website should have a spot for video on the homepage.

This website is for a very professional and well know photography company. Because it is photography the website needs to be VERY visual.

Site should be unique and really stand out to help sell the business and their services. EVERYTHING about this business is visual, so the site MUST reflect that.

Site Overall: Fun and Artistic. This is a forward thinking company that is fun, upbeat, and does things differently, they need the design to reflect that. This is a modern photography company.

They also do all kinds of photography from school kids, sports teams, in studio shoots with High School Seniors, Family Pictures etc.

Colors: We like the white background because it is clean and really helps the photos stand out. Also please look at the logo too. Use colors from that and make things flow. Again we want this to stand out and be different while at the same time being clean.

Menu: Horizontal. We like bold and easy to read menu items. Don’t make it small and cluttered. Include the same items that are in the other site for the mock up.

Site Structure: Clean and easy to navigate. We have a lot of content to display so we need a clean structure that breaks up the text and content areas.

Images: Please pull images from the current site. We can always replace the images of course, but if you show them “their own stuff” in the new design you will be closer to winning because it will feel more like “them”

Content Areas: It is a safe bet that if it is on the current site we need it on the new site. So don’t drop anything as it makes it hard to “cut content”.

What we don't want: We do not want clutter, boring, or templates or themes. We don’t want too cartoony, too cute, or too fancy. We don’t want ugly.

Out of respect to professional designers who really are working hard to win if you do not follow this brief, you submit worn out themes, templates, or boring designs you will be eliminated. We are offering great prize money for this so we expect great visual designs.

Thanks,

The Solvane Team

Target Market(s)

Target Market are upper middle class who want a better photography studio then the average studio, but don't want to go to the highest end of photography. This studio will cater to higher middle class.

Industry/Entity Type

Business

Number of Pages Required

1 page

Font styles to use
Sans Serif

Requirements
Must have
• Video on Home page
• Clean
• Stand Out
• Fun
• Professional
Nice to have
• Creative
• Lots of content in a great structure
Should not have
• clutter
• ugly design
• messy

```html
<!DOCTYPE html>
<html lang="en">
<head>
<meta charset="utf-8">
<title>Kelva Photography</title>
<link href="https://fonts.googleapis.com/css2?family=Source+Sans+3:wght@300;400;600&display=swap" rel="stylesheet">
<style>
:root{
  --pink:#c2397f;
  --blue:#3b4fb0;
  --ink:#333;
  --muted:#555;
  --rule:#bbb;
  --band:#e3e4e8;
  --white:#fff;
}
*{box-sizing:border-box;margin:0;padding:0}
html,body{width:800px;height:1200px;overflow:hidden;background:var(--white)}
body{font-family:"Source Sans 3",sans-serif;color:var(--ink);position:relative}
.abs{position:absolute}
.site-header{top:0;left:0;width:800px;height:72px;background:#f8f8f9}
.brand{left:28px;top:20px;font-size:28px;font-weight:400;color:var(--ink);display:flex;align-items:center;gap:8px}
.brand-dot{width:16px;height:16px;border-radius:50%;background:var(--pink)}
.main-nav{top:28px;left:0;width:800px;font-size:12px;font-weight:300;color:var(--ink)}
.main-nav span{position:absolute;white-space:nowrap}
.main-nav .active{color:var(--pink)}
.hero{top:72px;left:0;width:800px;height:370px}
.hero-title{left:29px;top:228px;font-size:25px;font-weight:300;line-height:24px;color:var(--ink)}
.hero-title strong{display:block;color:var(--pink);font-weight:400}
.hero-copy{left:29px;top:300px;font-size:15px;font-weight:300;line-height:22px;color:var(--ink);width:320px}
.btn{background:var(--blue);color:var(--white);font-size:11.5px;font-weight:400;display:flex;align-items:center;justify-content:center}
.btn-order{left:29px;top:354px;width:84px;height:25px}
.band{top:442px;left:0;width:800px;height:23px;background:var(--band)}
.welcome-title{left:30px;top:518px;font-size:20px;font-weight:300;line-height:22px}
.welcome-title span{display:block;color:var(--pink)}
.welcome-body{left:213px;top:488px;width:520px;font-size:13.5px;font-weight:300;line-height:17px;color:var(--ink)}
.welcome-body p{margin-bottom:16px}
.btn-read{left:214px;top:598px;width:76px;height:23px}
.video-section{top:635px;left:0;width:800px;height:367px;background:linear-gradient(#cfcbc8,#dedbd8 60%,#d6d3d1)}
.video-frame{left:30px;top:661px;width:492px;height:306px}
.about{left:534px;top:661px;width:235px;height:306px;background:var(--white);padding:16px 14px}
.about h2{font-size:19px;font-weight:300;color:var(--pink);padding-bottom:6px;border-bottom:1px solid var(--rule);margin-bottom:8px}
.about p{font-size:11px;font-weight:300;line-height:22.4px;color:var(--ink)}
.about p+p{margin-top:22px}
.footer-title{font-size:16px;font-weight:300;color:var(--pink);padding-bottom:6px;border-bottom:1px solid var(--rule)}
.f-menu{left:28px;top:1026px;width:311px}
.f-news{left:400px;top:1026px;width:168px}
.f-follow{left:602px;top:1026px;width:169px}
.f-links{font-size:11px;font-weight:300;color:var(--ink)}
.f-links span{position:absolute;white-space:nowrap}
.news-copy{left:398px;top:1066px;width:160px;font-size:10px;line-height:16px;font-weight:300}
.news-input{left:399px;top:1120px;width:171px;height:24px;border:1px solid #ccc;background:var(--white)}
.btn-sub{left:402px;top:1158px;width:76px;height:22px;font-size:11px}
.social{left:603px;top:1064px;font-size:18px;font-weight:400;color:var(--ink);display:flex;align-items:center;gap:10px}
.social i{display:block;width:18px;height:18px;background:var(--ink)}
.copyright{left:609px;top:1151px;font-size:10.5px;font-weight:300}
</style>
</head>
<body>
<header class="site-header abs">
  <div class="brand abs"><span class="brand-dot"></span>Kelva</div>
  <nav class="main-nav abs">
    <span class="active" style="left:293px">Home</span>
    <span style="left:351px">Studio</span>
    <span style="left:411px">Super Senior Days</span>
    <span style="left:524px">Book It!</span>
    <span style="left:588px">Ordering</span>
    <span style="left:660px">Sports</span>
    <span style="left:719px">Contact Us</span>
  </nav>
</header>

<section class="hero abs">
  <svg width="800" height="370" viewBox="0 0 800 370">
    <rect width="800" height="370" fill="#e4e6ee"/>
    <polygon points="0,0 327,0 548,370 0,370" fill="#6e4a4a" role="img" aria-label="Family group portrait in a studio"/>
    <polygon points="327,0 800,0 800,392 548,370" fill="#dde1ec" role="img" aria-label="Student portrait with a soft backdrop"/>
    <g role="img" aria-label="Sports team and player photographs">
      <polygon points="390,66 520,43 545,212 415,230" fill="#2a3c8f"/>
      <rect x="543" y="43" width="114" height="170" fill="#c9b7a8"/>
      <polygon points="684,46 790,78 755,237 650,206" fill="#8c96a6"/>
    </g>
    <polygon points="0,143 300,143 435,330 0,330" fill="#fff"/>
  </svg>
</section>
<h1 class="hero-title abs">School Photography and<strong>Dana Orrel Sports photography</strong></h1>
<p class="hero-copy abs">Click to order or contact our sports Department to Schedule your team!</p>
<div class="btn btn-order abs">Order Now</div>

<div class="band abs"></div>

<h2 class="welcome-title abs">Welcome to<span>Kelva Photography</span></h2>
<div class="welcome-body abs">
  <p>Kelva means to remember and for us, Kelva is the new brand name for one of a kind school photography and Dana Orrel sports photography.</p>
  <p>Please call us at (555)014-2287 ext 3 to shedule your event!</p>
  <p>Services offered will typically be done in volume settings. such services include:</p>
</div>
<div class="btn btn-read abs">Read more</div>

<section class="video-section abs" role="img" aria-label="Faded school building backdrop"></section>
<svg class="video-frame abs" viewBox="0 0 492 306">
  <rect x="0" y="0" width="209" height="306" fill="#8a2a4a" role="img" aria-label="Graduate portrait in cap and gown"/>
  <rect x="209" y="0" width="283" height="306" fill="#c9b9b2" role="img" aria-label="Senior portrait outdoors"/>
  <circle cx="253" cy="130" r="25" fill="none" stroke="#fff" stroke-width="3" opacity=".85"/>
  <polygon points="246,116 246,144 268,130" fill="#fff" opacity=".85"/>
  <rect x="87" y="265" width="330" height="30" rx="2" fill="#222" opacity=".75"/>
  <polygon points="108,272 108,288 121,280" fill="#fff"/>
  <rect x="159" y="273" width="196" height="12" fill="none" stroke="#ddd"/>
  <g fill="#3ea6e0"><rect x="364" y="273" width="2" height="12"/><rect x="368" y="273" width="2" height="12"/><rect x="372" y="273" width="2" height="12"/><rect x="376" y="273" width="2" height="12"/><rect x="380" y="273" width="2" height="12"/><rect x="384" y="273" width="2" height="12"/><rect x="388" y="273" width="2" height="12"/></g>
  <path d="M400 274h4M400 274v4M410 274h-4M410 274v4M400 285h4M400 285v-4M410 285h-4M410 285v-4" stroke="#fff" stroke-width="1.5"/>
</svg>
<aside class="about abs">
  <h2>About video</h2>
  <p>Home Studio Super Senior DaysBook It! Ordering Sports Contact Us</p>
  <p>If your high school has contracted with Kelva Photography to provide your senior yearbook photo, this video explains what options are available to you and how to prepare for your</p>
</aside>

<div class="f-menu abs"><div class="footer-title">Main menu</div></div>
<div class="f-links abs" style="left:0;top:0">
  <span style="left:37px;top:1067px">Home</span>
  <span style="left:37px;top:1091px">Contact Us</span>
  <span style="left:37px;top:1115px">Book It!</span>
  <span style="left:37px;top:1139px">Ordering</span>
  <span style="left:37px;top:1163px">Super Senior Days</span>
  <span style="left:224px;top:1067px">Privacy &amp; Terms</span>
  <span style="left:224px;top:1091px">Class of 2015 Info</span>
  <span style="left:224px;top:1115px">SportsKids</span>
  <span style="left:224px;top:1139px">Specials</span>
  <span style="left:224px;top:1163px">Studio</span>
</div>

<div class="f-news abs"><div class="footer-title">Newsletter</div></div>
<p class="news-copy abs">Enter your email and subscribe aour newsletter</p>
<div class="news-input abs"></div>
<div class="btn btn-sub abs">Subscribe</div>

<div class="f-follow abs"><div class="footer-title">Follow us</div></div>
<div class="social abs"><i></i>Snapshare</div>
<p class="copyright abs">Copyright © Kelva Photography</p>
</body>
</html>
```